Business Card Design

We currently have a business card design for our main business 'Lantern Wallcover"
We are reasonably happy with our current design for Lantern Wallcover business card (black damask patterned wallpaper in background white simplistic font with white chandelier (see logo on website). www.lanternwallcover.com.au

We are considering whether its in our best interest to have a separate business card OR a double sided card to promote our secondary business 'Quill Glow'. We are open to either a double-sided card with one business on each side OR a double sided card for each business. With contact info on the back of each.

We need a new snazzy design for 'Quill Glow' our custom made lampshades from which we craft from our wallpaper designs. We had an idea that we could use the top swatch shown on this link below as the pattern in the background (Orange/black) geometric triangles.
http://www.lanternwallcover.com.au/product_info.php?products_id=1086

For the quill glow Font we would be happy with something similar to Lantern Wallcover but perhaps a little more handmade/arty slant.
Below another link shows you a few of our lampshades
http://www.lanternwallcover.com.au/index.php?cPath=10

For Quill Glow I think we also need the quote under in smaller font
"Custom-Made Wallpaper Lampshades"

Target Market(s)

Quill Glow will be for the Young Funky Apartment Dwellers, Young Families Styling Home Decor and Kids Rooms. It also attracts small business owners doing shop-fits.

Industry/Entity Type

Business

Contact Information for Business Card

We need to incorporate our sister business to the back side of our business card. I am also open to having two different business cards if designers think this will not be possible.
We need the same contact info, different logo.
ABN: 47 302 916 854
Email: sales@lanternwallcover.com.au
Postal Address: PO Box 793, Larkfield VIC 3389
Website: http://www.lanternwallcover.com.au

Requirements
Must have
• A hand-made arty appeal for Quill Glow
Was unable to get sliders to work for the look and feel so below is the best list from the above:
Bold, Playful, Modern, Personable, Colorful, Upmarket.
Nice to have
• We love the bold contrasting colors. Colors chosen for our website were Orange, Blue and Duck Egg Bright Blue!

```html
<!DOCTYPE html>
<html lang="en">
<head>
<meta charset="utf-8">
<title>Lantern Wallcover and Quill Glow Business Cards</title>
<link href="https://fonts.googleapis.com/css2?family=Didact+Gothic&family=Poiret+One&display=swap" rel="stylesheet">
<style>
  :root {
    --page: #ffffff;
    --ink: #1e1e1e;
    --card-black: #000000;
    --damask-dark: #141414;
    --damask-mid: #3a3a3a;
    --white: #ffffff;
    --orange: #f26a1b;
    --duck-egg: #62c8e2;
    --border: #c9c9c9;
    --shadow: rgba(0, 0, 0, 0.55);
  }
  * { margin: 0; padding: 0; box-sizing: border-box; }
  html, body {
    width: 1200px; height: 848px; overflow: hidden;
    background: var(--page);
    font-family: "Didact Gothic", "Century Gothic", sans-serif;
  }
  .canvas { position: relative; width: 1200px; height: 848px; }

  /* Lantern Wallcover card */
  .card-lantern {
    position: absolute; left: 48px; top: 45px; width: 628px; height: 378px;
    background: var(--card-black);
    box-shadow: -6px 8px 10px var(--shadow);
  }
  .lantern-header {
    position: absolute; left: 0; top: 0; width: 100%; height: 136px;
    background: radial-gradient(ellipse at 50% 60%, var(--damask-mid), var(--damask-dark) 75%);
  }
  .lantern-rule {
    position: absolute; left: 0; top: 137px; width: 100%; height: 3px; background: var(--white);
  }
  .lantern-name {
    position: absolute; left: 15px; top: 28px;
    font-size: 40px; color: var(--white); letter-spacing: -0.5px; line-height: 1;
  }
  .lantern-contact {
    position: absolute; left: 150px; top: 264px; color: var(--white);
    font-size: 19.5px; line-height: 26.5px;
  }
  .lantern-contact .abn { padding-left: 58px; }
  .contact-line { display: flex; align-items: center; gap: 10px; }
  .icon { width: 18px; height: 18px; flex: none; }

  /* Quill Glow card */
  .card-quill {
    position: absolute; left: 543px; top: 362px; width: 630px; height: 378px;
    background: var(--white); border: 1px solid var(--border);
    box-shadow: -6px 8px 10px var(--shadow);
  }
  .quill-pattern {
    position: absolute; left: 16px; top: 12px; width: 169px; height: 353px;
    background: linear-gradient(160deg, var(--orange) 0%, var(--duck-egg) 35%, #2a2a2a 55%, var(--orange) 75%, var(--duck-egg) 100%);
  }
  .quill-name {
    position: absolute; right: 12px; top: 8px;
    font-family: "Poiret One", "Didact Gothic", sans-serif;
    font-size: 50px; color: #2b2b2b; letter-spacing: 1.5px; line-height: 1;
  }
  .quill-tagline {
    position: absolute; left: 272px; top: 68px;
    font-size: 17px; color: var(--duck-egg); letter-spacing: 0.2px;
  }
  .person {
    position: absolute; left: 340px; top: 164px; width: 270px; text-align: center; color: var(--ink);
  }
  .person-name { font-size: 33px; line-height: 38px; }
  .person-role { font-size: 24px; line-height: 34px; }
  .quill-contact {
    position: absolute; right: 12px; top: 262px; color: var(--ink);
    font-size: 19.5px; line-height: 26px; text-align: right;
  }
  .quill-contact .contact-line { justify-content: flex-end; }
  .quill-contact .phone { padding-right: 56px; }
</style>
</head>
<body>
<div class="canvas">

  <section class="card-lantern" aria-label="Lantern Wallcover card">
    <div class="lantern-header" role="img" aria-label="Black damask wallpaper pattern"></div>
    <div class="lantern-rule"></div>
    <h1 class="lantern-name">Lantern Wallcover</h1>
    <div class="lantern-contact">
      <p class="abn">ABN: 47 302 916 854</p>
      <p class="contact-line">
        <svg class="icon" viewBox="0 0 18 18"><circle cx="9" cy="9" r="8" fill="none" stroke="#fff" stroke-width="1.5"/><text x="9" y="13" font-size="11" text-anchor="middle" fill="#fff" font-family="sans-serif">@</text></svg>
        <span>sales@lanternwallcover.com.au</span>
      </p>
      <p class="contact-line">
        <svg class="icon" viewBox="0 0 18 18"><circle cx="9" cy="9" r="8" fill="none" stroke="#fff" stroke-width="1.5"/><rect x="4.5" y="6" width="9" height="6" fill="none" stroke="#fff" stroke-width="1.2"/><path d="M4.5 6 L9 9.5 L13.5 6" fill="none" stroke="#fff" stroke-width="1.2"/></svg>
        <span>PO Box 793, Larkfield VIC 3389</span>
      </p>
      <p class="contact-line">
        <svg class="icon" viewBox="0 0 18 18"><circle cx="9" cy="9" r="8" fill="none" stroke="#fff" stroke-width="1.5"/><ellipse cx="9" cy="9" rx="2.8" ry="5.5" fill="none" stroke="#fff" stroke-width="1"/><path d="M3.5 9 H14.5" stroke="#fff" stroke-width="1"/></svg>
        <span>www.lanternwallcover.com.au</span>
      </p>
    </div>
  </section>

  <section class="card-quill" aria-label="Quill Glow card">
    <div class="quill-pattern" role="img" aria-label="Orange, duck egg blue and black geometric triangle wallpaper pattern"></div>
    <h2 class="quill-name">Quill Glow</h2>
    <p class="quill-tagline">Custom-Made Wallpaper Lampshades</p>
    <div class="person">
      <p class="person-name">Nora Ellery</p>
      <p class="person-role">Sales</p>
    </div>
    <div class="quill-contact">
      <p class="contact-line phone">
        <svg class="icon" viewBox="0 0 18 18"><circle cx="9" cy="9" r="8" fill="none" stroke="#f26a1b" stroke-width="1.5"/><path d="M6 5 Q5 9 9 12.5 L11.5 11 L12.5 12.5 Q10 14.5 7 12 Q3.5 8 6 5 Z" fill="#f26a1b"/></svg>
        <span>+61 412 608 274</span>
      </p>
      <p class="contact-line">
        <svg class="icon" viewBox="0 0 18 18"><circle cx="9" cy="9" r="8" fill="none" stroke="#f26a1b" stroke-width="1.5"/><text x="9" y="13" font-size="11" text-anchor="middle" fill="#f26a1b" font-family="sans-serif">@</text></svg>
        <span>sales@lanternwallcover.com.au</span>
      </p>
      <p class="contact-line">
        <svg class="icon" viewBox="0 0 18 18"><circle cx="9" cy="9" r="8" fill="#f26a1b"/><rect x="4.5" y="6" width="9" height="6" fill="none" stroke="#fff" stroke-width="1.2"/><path d="M4.5 6 L9 9.5 L13.5 6" fill="none" stroke="#fff" stroke-width="1.2"/></svg>
        <span>PO Box 793, Larkfield VIC 3389</span>
      </p>
      <p class="contact-line">
        <svg class="icon" viewBox="0 0 18 18"><circle cx="9" cy="9" r="8" fill="#f26a1b"/><ellipse cx="9" cy="9" rx="2.8" ry="5.5" fill="none" stroke="#fff" stroke-width="1"/><path d="M3.5 9 H14.5" stroke="#fff" stroke-width="1"/></svg>
        <span>www.lanternwallcover.com.au</span>
      </p>
    </div>
  </section>

</div>
</body>
</html>
```